Mane Glow...restoring shine to tired, brittle locks!

We are launching a luxurious, all-natural line of handmade hair products. These products will compete against a host of other not-so natural products targeting women with coily, kinky curly hair and the desire to grow (or re-grow) their tresses. Our product is different and we want our brand to reflect that. Mane Glow is about bringing 'life back' to dry, damaged hair. Our product will be bottled in black or blue bottles and we'd love to see lime green accents in the concepts.

Target Market(s)

21 - 50 year old women with wavy, coily, curly or kinky hair.

Industry/Entity Type

Hair Care Product

Colors
add136
ffffff

Requirements
Must have
• Label must be "ready for retail" and catch a consumers eye when competing against other products. Should also look great online.
Nice to have
• Would love the label to include a symbol of "Life" or growth. The base of all the products is a plant called Moringa which is plant/superfood used in Africa and India. More information about Moringa can be found here
• http://www.plumtorvex.com/articles/amazing-benefits-of-moringa-plant/
• Some of the benefits of Moringa include:
• Builds collagen fibers and minimize the appearance of fine wrinkle lines (Vitamin A)
• - Minimizes the appearance of fine wrinkle lines. (Vitamin C)
• - Improves moisturizing, softness and smoothness. (Vitamin E)
• - Delays the aging process
• - Helps build collagen which improves skin conditions
• - Is a natural healing emollient
• - Helps with dry, rough skin conditions like eczema, psoriasis and dermatitis.
• - Protects your skin from environmental damage
• - Helps improve scalp circulation (which aids in preventing hair loss)
• - Helps improve split ends in hair

```html
<!DOCTYPE html>
<html lang="en">
<head>
<meta charset="utf-8">
<title>Mane Glow Natural Products – Label Set</title>
<link href="https://fonts.googleapis.com/css2?family=Didact+Gothic&family=Open+Sans:wght@400;700&display=swap" rel="stylesheet">
<style>
  :root {
    --lime: #add136;
    --white: #ffffff;
    --label-black: #141316;
    --label-plum: #221f27;
    --page: #ffffff;
  }
  * { box-sizing: border-box; margin: 0; padding: 0; }
  html, body { width: 1200px; height: 1000px; overflow: hidden; background: var(--page); }
  body { position: relative; font-family: "Didact Gothic", "Open Sans", sans-serif; color: var(--white); }

  .label { position: absolute; background: var(--label-black); overflow: hidden; }
  .frame { position: absolute; border: 1.5px solid var(--lime); }
  .brand { font-family: "Didact Gothic", sans-serif; color: var(--lime); text-align: center; white-space: nowrap; }
  .tagline-band { background: var(--lime); color: var(--label-black); text-align: center; font-family: "Didact Gothic", sans-serif; }
  .sprig {
    position: absolute;
    background: radial-gradient(ellipse at center, rgba(173,209,54,0.55) 0%, rgba(173,209,54,0.18) 55%, rgba(173,209,54,0) 75%);
  }
  .rule { height: 1.5px; background: var(--lime); margin: 0 auto; }

  /* Jar band label */
  .jar-label { left: 10px; top: 700px; width: 275px; height: 150px; background: var(--label-plum); }
  .jar-label .frame { inset: 10px 0 10px 0; border-left: none; border-right: none; }
  .jar-label .brand { position: absolute; top: 28px; left: 0; right: 0; font-size: 19px; }
  .jar-label .tagline-band { position: absolute; top: 60px; left: 22px; right: 0; font-size: 14px; padding: 7px 0; white-space: nowrap; }
  .jar-label .product-line { position: absolute; top: 106px; left: 0; right: 0; text-align: center; font-size: 11px; white-space: nowrap; }

  /* Lid round label */
  .lid-label { left: 295px; top: 590px; width: 280px; height: 280px; border-radius: 50%; background: var(--label-plum); }
  .lid-label .frame { inset: 8px; border-radius: 50%; }
  .lid-label .brand { position: absolute; top: 86px; left: 0; right: 0; font-size: 15px; }
  .lid-label .tagline-band { position: absolute; top: 110px; left: 18px; right: 18px; font-size: 13px; padding: 4px 0; white-space: nowrap; }
  .lid-label .product-name { position: absolute; top: 146px; left: 0; right: 0; text-align: center; font-size: 11px; }
  .lid-label .key-ingredients { position: absolute; top: 164px; left: 0; right: 0; text-align: center; font-family: "Open Sans", sans-serif; font-weight: 700; font-size: 16px; color: var(--lime); }
  .lid-label .benefit { position: absolute; top: 196px; left: 0; right: 0; text-align: center; font-size: 11px; line-height: 1.35; }
  .lid-label .web { position: absolute; top: 240px; left: 0; right: 0; text-align: center; font-size: 9px; }

  /* Bottle label */
  .bottle-label { left: 595px; top: 235px; width: 220px; height: 630px; }
  .bottle-label .frame { inset: 6px; }
  .bottle-label .brand { position: absolute; top: 28px; left: 0; right: 0; font-size: 18px; line-height: 1.3; }
  .bottle-label .tagline-band { position: absolute; top: 100px; left: 6px; right: 6px; font-size: 14px; line-height: 1.3; padding: 8px 6px; }
  .bottle-label .product-block { position: absolute; top: 225px; left: 0; right: 0; text-align: center; }
  .product-title { font-size: 14px; }
  .bottle-label .key-ingredients { font-family: "Open Sans", sans-serif; font-weight: 700; font-size: 14px; color: var(--lime); margin-top: 6px; }
  .bottle-label .use { font-size: 11px; line-height: 1.35; margin-top: 8px; }
  .bottle-label .rule { width: 60px; margin-top: 14px; }
  .claims { font-family: "Open Sans", sans-serif; font-weight: 700; font-size: 14px; color: var(--lime); line-height: 1.35; margin-top: 10px; }
  .bottle-label .rule.second { margin-top: 10px; }
  .bottle-label .care { font-size: 11px; line-height: 1.35; margin-top: 12px; }
  .bottle-label .volume { position: absolute; bottom: 20px; left: 0; right: 0; text-align: center; font-size: 11px; }

  /* Soap box label */
  .box-label { left: 845px; top: 560px; width: 335px; height: 270px; }
  .box-label .soap-window { position: absolute; left: 22px; top: 40px; width: 70px; height: 150px; border-radius: 70px 4px 70px 4px; background: linear-gradient(160deg, #3fbf8a, #1f8a5e); }
  .box-label .panel { position: absolute; left: 110px; top: 24px; width: 210px; height: 225px; }
  .box-label .frame { inset: 0; }
  .box-label .brand { position: absolute; top: 14px; left: 0; right: 0; font-size: 15px; }
  .box-label .tagline-band { position: absolute; top: 40px; left: 0; right: 0; font-size: 11px; padding: 4px 0; white-space: nowrap; }
  .box-label .copy { position: absolute; top: 68px; left: 8px; width: 120px; }
  .box-heading { font-family: "Open Sans", sans-serif; font-weight: 700; font-size: 11px; color: var(--lime); }
  .box-text { font-size: 7.5px; line-height: 1.35; margin-top: 2px; }
  .box-text strong { color: var(--lime); font-family: "Open Sans", sans-serif; }
  .box-heading.how { margin-top: 6px; }
</style>
</head>
<body>

  <section class="label jar-label">
    <div class="frame"></div>
    <div class="sprig" style="left:0; top:40px; width:36px; height:100px;" role="img" aria-label="Moringa sprig with lime and white leaves"></div>
    <p class="brand">Mane Glow Natural Products</p>
    <p class="tagline-band">Restore shine to tired, brittle locks</p>
    <p class="product-line">The Renewer Leave-in Conditioner with Moringa</p>
  </section>

  <section class="label lid-label">
    <div class="frame"></div>
    <div class="sprig" style="left:65px; top:18px; width:150px; height:66px;" role="img" aria-label="Branching moringa sprig with lime and white leaves"></div>
    <div class="sprig" style="left:14px; top:160px; width:60px; height:80px;" role="img" aria-label="Moringa sprig with lime leaves"></div>
    <div class="sprig" style="left:206px; top:160px; width:60px; height:80px;" role="img" aria-label="Moringa sprig with lime leaves"></div>
    <p class="brand">Mane Glow Natural Products</p>
    <p class="tagline-band">Restore shine to tired, brittle locks</p>
    <p class="product-name">The Renewer Leave-in Conditioner with</p>
    <p class="key-ingredients">Moringa and Shea</p>
    <p class="benefit">Intense moisture, repair<br>and growth treatment</p>
    <p class="web">www.maneglowbotanics.com</p>
  </section>

  <section class="label bottle-label">
    <div class="frame"></div>
    <p class="brand">Mane Glow<br>Natural Products</p>
    <p class="tagline-band">Restore shine to tired,<br>brittle locks</p>
    <div class="sprig" style="left:50px; top:160px; width:120px; height:55px;" role="img" aria-label="Moringa sprig with lime and white leaves"></div>
    <div class="product-block">
      <p class="product-title">The Revival</p>
      <p class="key-ingredients">Moringa and Castor oil</p>
      <p class="use">Daily, nourishing hair<br>and scalp oil</p>
      <div class="rule"></div>
      <p class="claims">ALL NATURAL<br>HAND-MADE<br>PARABEN-FREE</p>
      <div class="rule second"></div>
      <p class="care">For daily sealing and care of<br>all hair textures</p>
    </div>
    <div class="sprig" style="left:20px; top:495px; width:180px; height:100px;" role="img" aria-label="Branching moringa sprigs with lime and white leaves"></div>
    <p class="volume">4 oz (118 ml)</p>
  </section>

  <section class="label box-label">
    <div class="soap-window" role="img" aria-label="Leaf-shaped window showing green moringa soap bar"></div>
    <div class="panel">
      <div class="frame"></div>
      <p class="brand">Mane Glow Natural Products</p>
      <p class="tagline-band">Restore shine to tired, brittle locks</p>
      <div class="copy">
        <p class="box-heading">Twice Over</p>
        <p class="box-text">Moisturizing &amp; Conditioning Shampoo Bar with <strong>Moringa and Aloe Leaf</strong></p>
        <p class="box-heading how">How to use:</p>
        <p class="box-text">Great for travel. Wet hair and rub the bar from root to tip to lather. Rinse and repeat. Allow the bar to dry after each use.</p>
      </div>
      <div class="sprig" style="left:130px; top:80px; width:78px; height:140px;" role="img" aria-label="Moringa sprigs with lime and white leaves"></div>
      <div class="sprig" style="left:10px; top:178px; width:110px; height:44px;" role="img" aria-label="Low moringa sprigs with lime leaves"></div>
    </div>
  </section>

</body>
</html>
```